Brave Ladies - Fitness Retreat

Tri Fold Brochure & Double sided A4 version options, see attached mockup.

Target Market: Women 18-50, Asian mainly .

Kovo Fitness Presents - Brave Ladies Fitness Retreats:

Something communicating the spirit of getting fit, being strong, eating healthy and strong sense of the feminine.

Industry/Entity Type

Fitness

```html
<!DOCTYPE html>
<html lang="en">
<head>
<meta charset="utf-8">
<title>Brave Ladies Boot Camp Bali Retreats – Brochure Spread</title>
<link href="https://fonts.googleapis.com/css2?family=Oswald:wght@500;700&family=Arimo:ital,wght@0,400;0,700;1,700&family=Russo+One&display=swap" rel="stylesheet">
<style>
  :root{
    --stage:#2f2f31;
    --paper:#ffffff;
    --terms-bg:#f2f1ef;
    --red:#c8141b;
    --red-deep:#8e0c10;
    --maroon:#7a1418;
    --ink:#2a2a2a;
    --white:#ffffff;
  }
  *{margin:0;padding:0;box-sizing:border-box}
  html,body{width:1200px;height:598px;overflow:hidden;background:var(--stage)}
  .canvas{position:relative;width:1200px;height:598px;overflow:hidden;background:var(--stage)}
  .spread{position:absolute;left:204px;top:19px;width:792px;height:560px;background:var(--paper);box-shadow:0 6px 18px rgba(0,0,0,.45)}
  .spread-art{position:absolute;inset:0;width:792px;height:560px}

  .terms{position:absolute;left:18px;top:18px;width:236px;font-family:"Arimo",sans-serif;color:var(--ink)}
  .terms-title{font-family:"Russo One",sans-serif;font-size:16px;color:var(--maroon);letter-spacing:.3px;margin-bottom:10px}
  .terms-list{list-style:none;font-size:8.6px;line-height:10.6px}
  .terms-list li{position:relative;padding-left:7px}
  .terms-list li::before{content:"";position:absolute;left:0;top:3px;width:3px;height:5px;background:var(--red);border-radius:0 2px 2px 0}

  .contact{position:absolute;left:372px;top:372px;width:150px;font-family:"Arimo",sans-serif;color:var(--white);text-align:right}
  .contact-title{font-weight:700;font-style:italic;font-size:11px;letter-spacing:.6px;margin-bottom:10px}
  .contact-block{font-size:8.6px;line-height:13px;margin-bottom:10px}
  .contact-web{position:absolute;left:330px;top:530px;font-family:"Arimo",sans-serif;font-weight:700;font-size:13px;color:var(--white);letter-spacing:.2px}

  .brand{position:absolute;left:640px;top:20px;width:120px;text-align:center;font-family:"Oswald",sans-serif;font-weight:700;font-size:34px;line-height:1;color:var(--red);letter-spacing:2px}

  .cover-title{position:absolute;left:527px;top:466px;width:265px;text-align:center;font-family:"Oswald",sans-serif;font-weight:700;font-size:21px;line-height:26px;color:var(--white);letter-spacing:.5px;text-shadow:1px 2px 2px rgba(0,0,0,.55)}
</style>
</head>
<body>
<div class="canvas">
  <div class="spread">
    <svg class="spread-art" viewBox="0 0 792 560" xmlns="http://www.w3.org/2000/svg">
      <defs>
        <linearGradient id="red-fill" x1="0" y1="0" x2="1" y2="1">
          <stop offset="0" stop-color="#d81a20"/>
          <stop offset="1" stop-color="#8e0c10"/>
        </linearGradient>
        <linearGradient id="greenery" x1="0" y1="0" x2="1" y2="1">
          <stop offset="0" stop-color="#9bb673"/>
          <stop offset=".55" stop-color="#5f7f45"/>
          <stop offset="1" stop-color="#c9c2b8"/>
        </linearGradient>
        <linearGradient id="sand" x1="0" y1="0" x2="1" y2="1">
          <stop offset="0" stop-color="#8a847e"/>
          <stop offset="1" stop-color="#4f4a46"/>
        </linearGradient>
        <linearGradient id="path-scene" x1="0" y1="0" x2="0" y2="1">
          <stop offset="0" stop-color="#dfe7ea"/>
          <stop offset=".35" stop-color="#7f9f5e"/>
          <stop offset=".8" stop-color="#d9d3c9"/>
        </linearGradient>
      </defs>

      <!-- inside left panel -->
      <rect x="0" y="0" width="264" height="400" fill="var(--terms-bg)"/>
      <!-- inside middle top photo -->
      <rect x="264" y="0" width="263" height="320" fill="url(#greenery)" role="img" aria-label="Photo: women practising boxing with pink gloves among tropical plants"/>
      <!-- sand workout photo -->
      <path d="M0,368 C180,358 300,323 380,263 C450,208 500,123 527,63 L527,560 L0,560 Z" fill="url(#sand)" role="img" aria-label="Photo: women doing floor exercises on a black sand beach"/>
      <!-- red swoosh band -->
      <path d="M0,345 C180,335 300,300 380,240 C450,185 500,100 527,40 L527,58 C500,118 450,203 380,258 C300,318 180,353 0,363 Z" fill="url(#red-fill)"/>
      <path d="M0,363 C180,353 300,318 380,258 C450,203 500,118 527,58 L527,64 C500,124 450,209 380,264 C300,324 180,359 0,369 Z" fill="#ffffff"/>
      <!-- middle circle photo -->
      <ellipse cx="361" cy="193" rx="68" ry="57" fill="#ffffff"/>
      <ellipse cx="361" cy="193" rx="63" ry="52" fill="#7d9a5c" role="img" aria-label="Photo: women stretching arms outdoors"/>
      <!-- contact red area -->
      <path d="M205,560 C245,445 370,362 527,318 L527,560 Z" fill="#ffffff"/>
      <path d="M220,560 C260,450 380,370 527,330 L527,560 Z" fill="url(#red-fill)"/>

      <!-- cover panel -->
      <rect x="527" y="0" width="265" height="420" fill="url(#path-scene)" role="img" aria-label="Photo: women running drills on a path lined with palm trees"/>
      <rect x="640" y="14" width="120" height="46" fill="#ffffff" opacity=".85"/>
      <path d="M527,452 C620,432 712,388 792,318 L792,560 L527,560 Z" fill="#e6e6e6"/>
      <path d="M527,464 C620,446 712,402 792,332 L792,560 L527,560 Z" fill="url(#red-fill)"/>
      <circle cx="636" cy="384" r="62" fill="#ffffff"/>
      <circle cx="636" cy="384" r="57" fill="#6f8f4d" role="img" aria-label="Photo: two women sparring with boxing pads on grass"/>

      <!-- fold lines -->
      <line x1="264" y1="0" x2="264" y2="560" stroke="#000" stroke-opacity=".08"/>
      <line x1="527" y1="0" x2="527" y2="560" stroke="#000" stroke-opacity=".12"/>
    </svg>

    <section class="terms">
      <h2 class="terms-title">TERMS AND CONDITIONS</h2>
      <ul class="terms-list">
        <li>Travel Insurance is mandatory for all of our guests</li>
        <li>Please confirm any special dietary needs before booking. Please note that for reasons of safety we cannot take guests who have a fatal allergy to any food/food groups. We are unable to provide separate meals and are very aware that the closest hospital may be up to 2 hours away.</li>
        <li>All clients to complete a Fitness &amp; Health Assessment from Trainer and to be completed prior to booking.</li>
        <li>Installment Payment is possible</li>
        <li>To secure your retreat we require a non-refundable deposit of $500pp</li>
        <li>Final payment to be made 30 days prior to arrival date. Cancellation fees may apply</li>
        <li>All funds are non-refundable if a guest chooses to cancel within 30 days of retreat start date.</li>
        <li>Refunds/credits will not be given after journey commencement, even if services, activities or meals are unused or cancelled for any reason</li>
        <li>Personal expenses to be paid in cash at end of retreat (laundry, drinks etc)</li>
        <li>We operate rain, hail or shine!</li>
      </ul>
    </section>

    <section class="contact">
      <h3 class="contact-title">FURTHER INFO:</h3>
      <p class="contact-block">MARISA<br>+62 811.4402.7186<br>marisa.kovofitness@mail.com</p>
      <p class="contact-block">Email : info@sunrisebali.com<br>Mob : +62 813 5520 8841<br>Web : www.sunrisebali.com</p>
    </section>
    <p class="contact-web">WWW.KOVO-FITNESS.COM</p>

    <div class="brand">KOVO</div>
    <h1 class="cover-title">BRAVE LADIES BOOT<br>CAMP BALI RETREATS</h1>
  </div>
</div>
</body>
</html>
```